Blue Heron IT Business Card - Clean, Simple

Need a simple, clean standard sized business card for an IT consulting business using existing logo and company colours. Background should be mainly white. Feel free to be creative but clean, simple, quiet design is preferred. Font is specified in logo but any sans serif fonts work.

Contact Information for card is as follows (doesn't need to be in this exact order):

Malcolm Pettigrew
Owner
malcolm@blueheronit.ca
705-412-9083
www.blueheronit.ca

Target Market(s)

Small to medium sized business.

Industry/Entity Type

IT Consulting

Contact Information for Business Card

Logo and contact info.

Font styles to use
Sans Serif

Colors
EE7325
F08F49
F5BC92
FAE3D3
FDF4ED

Requirements
Must have
• All white or mostly white background.

```html
<!DOCTYPE html>
<html lang="en">
<head>
<meta charset="utf-8">
<title>Blue Heron IT – Business Card</title>
<link rel="stylesheet" href="https://fonts.googleapis.com/css2?family=Montserrat:wght@300;500;600;700&display=swap">
<style>
  :root {
    --brand-orange: #EE7325;
    --brand-orange-light: #F08F49;
    --ink: #2a2a2a;
    --ink-soft: #4a4a4a;
    --paper: #ffffff;
    --backdrop: #e9e9e9;
  }
  * { box-sizing: border-box; margin: 0; padding: 0; }
  html, body {
    width: 1200px;
    height: 900px;
    overflow: hidden;
  }
  body {
    background: var(--backdrop);
    font-family: "Montserrat", Arial, sans-serif;
    display: flex;
    flex-direction: column;
    align-items: center;
    justify-content: center;
    gap: 40px;
  }
  .card {
    position: relative;
    width: 700px;
    height: 400px;
    box-shadow: 0 6px 18px rgba(0, 0, 0, 0.12);
  }

  /* Back side */
  .card--back {
    background: var(--brand-orange);
    display: flex;
    align-items: center;
    justify-content: center;
  }
  .card--back .wordmark {
    color: var(--paper);
  }

  /* Front side */
  .card--front {
    background: var(--paper);
    color: var(--ink);
  }
  .wordmark {
    font-weight: 600;
    font-size: 34px;
    letter-spacing: -0.5px;
    color: var(--ink);
    line-height: 1;
  }
  .card--front .wordmark {
    position: absolute;
    left: 0;
    right: 0;
    top: 181px;
    text-align: center;
  }
  .holder {
    position: absolute;
    left: 38px;
    top: 40px;
  }
  .holder__name {
    font-weight: 700;
    font-size: 22px;
    letter-spacing: 0.4px;
    text-transform: uppercase;
  }
  .holder__role {
    font-weight: 300;
    font-size: 19px;
    color: var(--ink-soft);
    margin-top: 2px;
  }
  .contact {
    position: absolute;
    font-weight: 500;
    font-size: 16px;
    letter-spacing: 0.6px;
  }
  .contact--web   { right: 38px; top: 45px; }
  .contact--phone { left: 38px;  bottom: 40px; }
  .contact--email { right: 38px; bottom: 40px; }

  .edge-bar {
    position: absolute;
    top: 144px;
    width: 12px;
    height: 108px;
    background: var(--brand-orange);
  }
  .edge-bar--left  { left: 0; }
  .edge-bar--right { right: 0; }
</style>
</head>
<body>
  <section class="card card--back" aria-label="Card back">
    <div class="wordmark">Blue Heron IT</div>
  </section>

  <section class="card card--front" aria-label="Card front">
    <div class="holder">
      <div class="holder__name">Malcolm Pettigrew</div>
      <div class="holder__role">owner</div>
    </div>
    <div class="contact contact--web">www.blueheronit.ca</div>

    <span class="edge-bar edge-bar--left"></span>
    <div class="wordmark">Blue Heron IT</div>
    <span class="edge-bar edge-bar--right"></span>

    <div class="contact contact--phone">705-412-9083</div>
    <div class="contact contact--email">malcolm@blueheronit.ca</div>
  </section>
</body>
</html>
```